Namibia currently imports 60% of its food. Yield Forward Tarvenia is an initiative which will assist Namibia to become self sustainable in terms of food production. We aim to do this through the development of 3 agricultural production zones which will include farming zones, local farmer assistance, processing and distribution of the final products. Please see our project overview attached.

```html
<!DOCTYPE html>
<html lang="en">
<head>
<meta charset="utf-8">
<title>Yield Forward Tarvenia</title>
<link href="https://fonts.googleapis.com/css2?family=Cormorant+Garamond:wght@600;700&family=Open+Sans:wght@400;600;700&display=swap" rel="stylesheet">
<style>
:root{
  --green:#0b6b3a;
  --green-dark:#07572f;
  --green-bright:#12a05a;
  --blue:#2b8fd3;
  --blue-light:#4fb0e6;
  --tan:#dfcdb9;
  --tan-card:#c4a78a;
  --mint:#cde0d8;
  --ink:#1f1f1f;
  --text:#4a4a4a;
  --white:#ffffff;
}
*{box-sizing:border-box;margin:0;padding:0}
html,body{width:1200px;height:3451px;overflow:hidden}
body{font-family:"Open Sans",Arial,sans-serif;color:var(--text);background:var(--white);position:relative}
.serif{font-family:"Cormorant Garamond",Georgia,serif;font-weight:700;color:var(--ink);text-transform:uppercase;letter-spacing:.5px}
.btn{display:inline-block;background:var(--blue);color:#fff;border-radius:22px;font-weight:600;font-size:15px;padding:11px 26px;text-decoration:none}
p{font-size:15px;line-height:28px}

/* header */
.site-header{position:absolute;top:0;left:0;width:1200px;height:97px;background:#fff;border-bottom:1px solid #eee}
.brand{position:absolute;left:111px;top:32px;display:flex;align-items:center;gap:10px;font-size:22px;font-weight:600;color:var(--green)}
.brand-dot{width:14px;height:14px;border-radius:50%;background:var(--green)}
.main-nav{position:absolute;left:485px;top:44px;display:flex;gap:24px;font-size:15px;color:#333}
.main-nav .active{color:var(--green);font-weight:600}
.quote-btn{position:absolute;left:943px;top:33px;height:43px;width:146px;text-align:center;padding:11px 0}

/* hero */
.hero{position:absolute;top:97px;left:0;width:1200px;height:470px;background:linear-gradient(180deg,#dfe3df 0%,#c9cfbf 20%,#5d8a3a 34%,#2f6b1f 60%,#1e4f16 100%)}
.hero-title{position:absolute;top:235px;left:0;width:1200px;text-align:center;color:#fff;font-size:54px;line-height:74px}
.hero-chevron{position:absolute;left:585px;top:390px}
.edge{position:absolute;left:0;width:1200px}

/* needs */
.needs h2{position:absolute;left:111px;top:640px;font-size:46px;line-height:56px}
.needs .copy{position:absolute;left:111px;top:768px;width:490px;font-size:15px}
.needs .copy p+p{margin-top:8px}
.needs .btn{position:absolute;left:111px;top:1111px}
.arch-photo{position:absolute;border-radius:0 8px 8px 8px;overflow:hidden}
.needs-photo{left:661px;top:654px;width:428px;height:498px;border-top-left-radius:260px;background:linear-gradient(160deg,#8fb4d1 0%,#c2cbb5 40%,#9c8a6c 75%,#7c6550 100%)}
.arch-line{position:absolute}

/* solution */
.solution{position:absolute;top:1260px;left:0;width:1200px;height:608px;background:var(--tan)}
.solution h2{position:absolute;top:70px;left:0;width:1200px;text-align:center;font-size:46px;line-height:56px}
.solution .lead{position:absolute;top:196px;left:240px;width:720px;text-align:center}
.solution .lead strong{color:var(--ink);font-weight:600}
.region{position:absolute;top:325px;width:260px;text-align:center}
.region-map{height:125px;margin:0 auto;border-radius:10px;background:linear-gradient(135deg,var(--green-bright),var(--green))}
.region h3{margin-top:22px;font-size:19px;font-weight:600;color:var(--ink)}
.region span{display:block;margin-top:8px;font-size:19px;color:#333}

/* focus */
.focus h2{position:absolute;left:111px;top:2082px;font-size:46px;line-height:56px}
.focus .copy{position:absolute;left:111px;top:2150px;width:490px}
.focus-card{position:absolute;left:625px;width:464px;height:126px;border-radius:80px 8px 80px 8px;color:#fff;padding:20px 0 0 126px}
.focus-card h3{font-size:17px;font-weight:700;letter-spacing:.3px}
.focus-card p{font-size:15px;line-height:24px;margin-top:6px}
.focus-card svg{position:absolute;left:38px;top:32px}
.card-farm{top:1961px;background:linear-gradient(90deg,var(--green-bright),var(--green))}
.card-assist{top:2096px;background:var(--tan-card)}
.card-assist h3{color:#fff}
.card-assist p{color:#f3ece3}
.card-logistics{top:2231px;background:linear-gradient(90deg,var(--blue-light),var(--blue))}

/* education */
.education{position:absolute;top:2435px;left:0;width:1200px;height:720px;background:var(--mint)}
.edu-photo{left:113px;top:70px;width:428px;height:498px;border-radius:8px 260px 8px 8px;background:linear-gradient(170deg,#7f9b5a 0%,#a37b62 40%,#5b6d4a 75%,#3c4c35 100%)}
.education h2{position:absolute;left:600px;top:115px;font-size:46px;line-height:56px}
.education .quote{position:absolute;left:600px;top:243px;width:490px;color:var(--ink);font-weight:600}
.education .copy{position:absolute;left:600px;top:310px;width:490px}
.education .btn{position:absolute;left:600px;top:472px}

/* footer */
.site-footer{position:absolute;top:3130px;left:0;width:1200px;height:281px;background:var(--green);color:#fff}
.footer-brand{position:absolute;left:111px;top:70px;width:220px;font-size:22px;font-weight:600;line-height:30px}
.socials{position:absolute;left:146px;top:232px;display:flex;gap:9px}
.socials span{width:30px;height:30px;border:1.5px solid #fff;border-radius:50%}
.footer-col{position:absolute;top:58px}
.footer-col h4{font-size:16px;font-weight:700;letter-spacing:.3px;margin-bottom:16px}
.footer-col li{list-style:none;font-size:15px;line-height:30px}
.contact-row{display:flex;gap:16px;font-size:15px;line-height:30px;margin-bottom:10px}
.contact-row svg{flex:none;margin-top:8px}
.divider{position:absolute;top:130px;width:1px;height:40px;background:rgba(255,255,255,.35)}
.copyright{position:absolute;top:3411px;left:0;width:1200px;height:40px;background:var(--green-dark);color:#fff;font-size:13px;text-align:center;line-height:40px}
</style>
</head>
<body>

<header class="site-header">
  <div class="brand"><span class="brand-dot"></span>Yield Forward Tarvenia</div>
  <nav class="main-nav">
    <span class="active">Home</span><span>About Us</span><span>Solutions</span><span>Education</span><span>Contact Us</span>
  </nav>
  <a class="btn quote-btn">Get a Quote</a>
</header>

<section class="hero" role="img" aria-label="Green crop rows stretching to the horizon with a tractor spraying the field">
  <h1 class="hero-title serif">An KVR Agri-Tech, Food<br>Security Initiative</h1>
  <svg class="hero-chevron" width="30" height="18" viewBox="0 0 30 18"><path d="M2 2 L15 15 L28 2" fill="none" stroke="#fff" stroke-width="2.5"/></svg>
</section>
<svg class="edge" style="top:515px" width="1200" height="55" viewBox="0 0 1200 55" preserveAspectRatio="none">
  <path d="M0 20 L40 17 L60 22 L110 14 L160 18 L210 12 L260 16 L300 22 L350 26 L420 30 L480 33 L540 32 L600 30 L660 31 L720 28 L780 24 L840 20 L900 17 L960 14 L1010 18 L1060 12 L1110 16 L1160 13 L1200 18 L1200 55 L0 55 Z" fill="#fff"/>
</svg>

<section class="needs">
  <h2 class="serif">Namibia Needs<br>Food</h2>
  <div class="copy">
    <p>Namibia is a young democracy in Sub-Saharan Africa with a population of approximately 2.5 Million people. The country’s agricultural sector has been slow to keep up with the increasing population. As a consequence, approximately 60% of the food required to feed the nation is imported. The elevated cost of these imported foods means a large proportion of the population consume food with low nutritional value.</p>
    <p>Despite vast tracts of available arable land and abundant water resources (both above and below ground), the agricultural sector has struggled to capitalise. This is largely due to a lack of investment, technical knowledge and available technologies</p>
  </div>
  <a class="btn">Learn More</a>
  <svg class="arch-line" style="left:661px;top:654px" width="330" height="330" viewBox="0 0 330 330"><path d="M2 330 L2 262 A260 260 0 0 1 262 2 L330 2" fill="none" stroke="var(--green)" stroke-width="8"/></svg>
  <div class="arch-photo needs-photo" role="img" aria-label="Farmer in a checked shirt and cap harvesting potatoes into a bucket in a field"></div>
</section>

<section class="solution">
  <h2 class="serif">The “Yield Forward”<br>Solution</h2>
  <p class="lead">The long term intention of the <strong>Yield Forward Tarvenia</strong> program would be to establish 3 distinct food production and processing zones which have access to large amounts of arable land, with high quality soil and strong water resources, as well as good transport connections to relevant markets. They are:</p>
  <div class="region" style="left:139px"><div class="region-map" style="width:180px" role="img" aria-label="Map outline of the Otavi region"></div><h3>Otavi Region</h3><span>Central Namibia</span></div>
  <div class="region" style="left:469px"><div class="region-map" style="width:244px" role="img" aria-label="Map outline of the Kavango region"></div><h3>Kavango Region</h3><span>North Namibia</span></div>
  <div class="region" style="left:800px"><div class="region-map" style="width:148px" role="img" aria-label="Map outline of the Neckartal Dam area"></div><h3>Neckartal Dam</h3><span>South Namibia</span></div>
</section>

<section class="focus">
  <h2 class="serif">Our Focus Areas</h2>
  <p class="copy">Yield Forward Tarvenia is an initiative which will assist Namibia to become self sustainable in terms of food production. We aim to do this through the development of 3 agricultural production zones which will include</p>

  <div class="focus-card card-farm">
    <svg width="60" height="60" viewBox="0 0 60 60" fill="none" stroke="#fff" stroke-width="3"><path d="M20 48 V26 M20 32 C12 30 8 24 8 20 C14 20 20 24 20 32 M20 30 C28 28 32 22 32 18 C26 18 20 22 20 30"/><path d="M38 46 L48 14 M44 10 L52 13 L50 19 L43 17 Z"/><path d="M4 50 H56"/></svg>
    <h3>FARMING ZONES</h3>
    <p>Lorem ipsum dolor sit amet, consectetur adipiscing elit, sed do eiusmod tempor</p>
  </div>
  <div class="focus-card card-assist">
    <svg width="60" height="60" viewBox="0 0 60 60" fill="#fff"><circle cx="50" cy="14" r="5"/><rect x="14" y="20" width="12" height="18" rx="4"/><path d="M16 38 L10 54 H15 L21 40 L26 54 H31 L25 38 Z"/><path d="M24 26 L44 50" stroke="#fff" stroke-width="3"/><path d="M38 52 H56" stroke="#fff" stroke-width="3"/></svg>
    <h3>LOCAL FARMER ASSISTANCE</h3>
    <p>Lorem ipsum dolor sit amet, consectetur adipiscing elit, sed do eiusmod tempor</p>
  </div>
  <div class="focus-card card-logistics">
    <svg width="64" height="60" viewBox="0 0 64 60" fill="none" stroke="#fff" stroke-width="3"><rect x="14" y="16" width="28" height="22" rx="2"/><path d="M42 22 H52 L58 30 V38 H42"/><circle cx="22" cy="42" r="5" fill="#2b8fd3"/><circle cx="50" cy="42" r="5" fill="#2b8fd3"/><path d="M2 22 H10 M4 28 H10 M6 34 H10"/></svg>
    <h3>PROCESSING AND DISTRIBUTION</h3>
    <p>Lorem ipsum dolor sit amet, consectetur adipiscing elit, sed do eiusmod tempor</p>
  </div>
</section>

<section class="education">
  <svg class="arch-line" style="left:211px;top:66px" width="334" height="334" viewBox="0 0 334 334"><path d="M0 2 L72 2 A260 260 0 0 1 332 262 L332 334" fill="none" stroke="var(--green)" stroke-width="8"/></svg>
  <div class="arch-photo edu-photo" role="img" aria-label="Smiling young woman carrying a basket of fresh cabbages in a vegetable field"></div>
  <h2 class="serif">Yield Forward<br>Education</h2>
  <p class="quote">“Give a man a fish and feed him for a day, teach a man to fish and feed him for a lifetime”</p>
  <p class="copy">Education is key to empowerment and we embrace that concept. As such, we aim to offer a vocational education scheme for the participants in the Yield Forward Tarvenia program. We aim to furnish the participants with the skills to be successful and sustainable farmers in their own rights.</p>
  <a class="btn">Learn More</a>
</section>

<svg class="edge" style="top:3085px" width="1200" height="50" viewBox="0 0 1200 50" preserveAspectRatio="none">
  <path d="M0 50 L0 36 L50 40 L100 34 L160 38 L220 30 L280 26 L340 22 L400 18 L460 16 L520 18 L580 15 L640 17 L700 14 L760 20 L820 24 L880 28 L940 32 L1000 36 L1060 32 L1120 38 L1160 34 L1200 38 L1200 50 Z" fill="var(--green)"/>
</svg>
<footer class="site-footer">
  <div class="footer-brand">Yield Forward<br>Tarvenia</div>
  <div class="socials"><span></span><span></span><span></span><span></span></div>

  <div class="footer-col" style="left:426px">
    <h4>CONTACTS</h4>
    <div class="contact-row"><svg width="16" height="20" viewBox="0 0 16 20"><path d="M8 0 C3.6 0 0 3.4 0 7.8 C0 13 8 20 8 20 C8 20 16 13 16 7.8 C16 3.4 12.4 0 8 0Z" fill="var(--tan-card)"/><circle cx="8" cy="8" r="3" fill="var(--green)"/></svg><span>Yield Forward Tarvenia,<br>Address Comes Here</span></div>
    <div class="contact-row"><svg width="18" height="18" viewBox="0 0 18 18"><path d="M4 1 L7 5 L5 7 C6 10 8 12 11 13 L13 11 L17 14 L15 17 C8 17 1 10 1 3 Z" fill="var(--tan-card)"/></svg><span>+1-555-010-0199</span></div>
    <div class="contact-row"><svg width="18" height="14" viewBox="0 0 18 14"><rect width="18" height="14" rx="2" fill="var(--tan-card)"/><path d="M1 2 L9 8 L17 2" fill="none" stroke="var(--green)" stroke-width="1.5"/></svg><span>info@yieldforwardtarvenia.com</span></div>
  </div>
  <div class="divider" style="left:677px"></div>
  <div class="footer-col" style="left:752px">
    <h4>QUICK LINKS</h4>
    <ul><li>Home</li><li>About</li><li>Solutions</li><li>Education</li></ul>
  </div>
  <div class="divider" style="left:913px"></div>
  <div class="footer-col" style="left:981px">
    <h4>OTHER LINKS</h4>
    <ul><li>Contact Us</li><li>Terms</li><li>Privacy Policy</li></ul>
  </div>
</footer>
<div class="copyright">Copyright ©2024 Yield Forward Tarvenia. All Rights Reserved.</div>

</body>
</html>
```